Business Card Design Project

Construction

Industry/Entity Type

Business

I've had the same logo for about 5 years. The logo itself is fine, however I'm looking to get a new design on the card. The green for the log is fine but the grey for the rest of the card is kind of dark and blah. Would like a new look. I'll send the file with the logo.

```html
<!DOCTYPE html>
<html lang="en">
<head>
<meta charset="utf-8">
<title>Clearline Commercial Builders – Business Cards</title>
<link href="https://fonts.googleapis.com/css2?family=Roboto:wght@400;500;700;900&family=Roboto+Condensed:wght@700&display=swap" rel="stylesheet">
<style>
  :root {
    --stage: #2b2b2b;
    --card-white: #f7f7f7;
    --card-grey: #58595b;
    --card-grey-dark: #4a4b4d;
    --green: #1fbf4a;
    --green-dark: #0a7a2a;
    --green-light: #5ef07f;
    --ink: #111111;
    --ink-soft: #444444;
    --on-grey: #ffffff;
    --seal: #1a1a1a;
  }
  * { box-sizing: border-box; margin: 0; padding: 0; }
  html, body { width: 1200px; height: 886px; overflow: hidden; }
  body {
    background: var(--stage);
    font-family: "Roboto", Arial, sans-serif;
    position: relative;
  }
  .card {
    position: absolute;
    left: 260px;
    width: 680px;
    height: 389px;
    background: var(--card-white);
    overflow: hidden;
    box-shadow: 0 10px 24px rgba(0,0,0,.45);
  }
  .card--back { top: 34px; }
  .card--front { top: 462px; }
  .card__shapes { position: absolute; inset: 0; }

  .brand { position: absolute; }
  .brand__row { display: flex; align-items: center; gap: 10px; }
  .brand__mark { width: 22px; height: 22px; background: var(--green); }
  .brand__name, .brand__sub {
    font-family: "Roboto", Arial, sans-serif;
    font-weight: 900;
    color: var(--ink);
    line-height: 1;
  }
  .brand__name { font-size: 40px; letter-spacing: .5px; }
  .brand__sub { font-size: 14px; letter-spacing: 1.6px; margin-top: 4px; margin-left: 32px; }

  /* back card */
  .back__brand { left: 34px; top: 150px; }
  .back__contact {
    position: absolute; left: 40px; top: 230px;
    font-size: 16px; line-height: 22px; color: var(--ink-soft);
  }
  .back__contact .gap { margin-top: 10px; }
  .back__info {
    position: absolute; right: 32px; top: 26px;
    text-align: right; color: var(--on-grey);
  }
  .heading {
    font-family: "Roboto Condensed", "Arial Narrow", sans-serif;
    font-weight: 700; color: var(--green); font-size: 18px;
    text-transform: uppercase; letter-spacing: .5px;
  }
  .license-list { list-style: none; font-size: 14px; line-height: 19px; margin: 4px 0 12px; }
  .license-list li::after {
    content: ""; display: inline-block; width: 8px; height: 8px;
    background: var(--on-grey); margin-left: 8px; vertical-align: 1px;
  }
  .codes { font-size: 14px; line-height: 19px; margin-top: 4px; }
  .seals { display: flex; justify-content: flex-end; gap: 12px; margin-top: 16px; }
  .seal { width: 56px; height: 56px; border-radius: 50%; background: var(--seal); border: 3px solid #d9d9d9; }

  /* front card */
  .front__person {
    position: absolute; left: 40px; top: 100px; color: var(--on-grey);
  }
  .person__name {
    font-family: "Roboto Condensed", "Arial Narrow", sans-serif;
    font-weight: 700; font-size: 26px; text-transform: uppercase;
  }
  .person__title {
    font-family: "Roboto Condensed", "Arial Narrow", sans-serif;
    font-weight: 700; font-size: 18px; color: var(--green); text-transform: uppercase;
  }
  .person__email { font-size: 15px; margin-top: 4px; }
  .phones { list-style: none; font-size: 17px; line-height: 22px; margin-top: 14px; }
  .phones li { display: flex; align-items: center; gap: 8px; }
  .phones svg { width: 14px; height: 14px; fill: var(--on-grey); }
  .service-area {
    font-family: "Roboto Condensed", "Arial Narrow", sans-serif;
    font-weight: 700; font-size: 18px; line-height: 21px;
    color: var(--green); text-transform: uppercase; margin-top: 14px;
  }
  .years-badge {
    width: 150px; height: 46px; margin-top: 16px;
    background: linear-gradient(#e9e9e9, #a9a9a9);
    border-radius: 6px;
  }
  .front__brand { right: 40px; top: 130px; }
  .front__license { position: absolute; right: 110px; top: 232px; font-size: 16px; color: var(--ink-soft); }
</style>
</head>
<body>

<section class="card card--back" aria-label="Card back">
  <svg class="card__shapes" viewBox="0 0 680 389" preserveAspectRatio="none">
    <defs>
      <linearGradient id="bandA" x1="0" y1="0" x2="1" y2="1">
        <stop offset="0" stop-color="var(--green-dark)"/>
        <stop offset=".5" stop-color="var(--green-light)"/>
        <stop offset="1" stop-color="var(--green-dark)"/>
      </linearGradient>
    </defs>
    <polygon points="262,0 680,0 680,389 610,389" fill="var(--card-grey)"/>
    <polygon points="246,0 266,0 614,389 592,389" fill="url(#bandA)"/>
  </svg>

  <div class="brand back__brand">
    <div class="brand__row"><span class="brand__mark"></span><span class="brand__name">CLEARLINE</span></div>
    <div class="brand__sub">COMMERCIAL BUILDERS</div>
  </div>

  <div class="back__contact">
    <div>(555) 014-2830</div>
    <div>(555) 014-7716</div>
    <div>CLEARLINECOMMERCIAL.com</div>
    <div class="gap">LICENSED, BONDED, INSURED</div>
    <div>LICENSE# 1004821</div>
  </div>

  <div class="back__info">
    <h3 class="heading">Licenses</h3>
    <ul class="license-list">
      <li>A - General Engineering</li>
      <li>B - General Building</li>
      <li>C21 - Demo/Bldg moving</li>
      <li>C36 - Plumbing</li>
    </ul>
    <h3 class="heading">NAICS Codes</h3>
    <p class="codes">236220, 238110, 236118<br>23810, 238350, 238390<br>327320</p>
    <div class="seals"><span class="seal"></span><span class="seal"></span></div>
  </div>
</section>

<section class="card card--front" aria-label="Card front">
  <svg class="card__shapes" viewBox="0 0 680 389" preserveAspectRatio="none">
    <defs>
      <linearGradient id="bandB" x1="0" y1="0" x2="1" y2="0">
        <stop offset="0" stop-color="var(--green-dark)"/>
        <stop offset=".5" stop-color="var(--green-light)"/>
        <stop offset="1" stop-color="var(--green-dark)"/>
      </linearGradient>
      <linearGradient id="greyB" x1="0" y1="0" x2="1" y2="1">
        <stop offset="0" stop-color="var(--card-grey)"/>
        <stop offset="1" stop-color="var(--card-grey-dark)"/>
      </linearGradient>
    </defs>
    <polygon points="0,0 316,0 356,389 0,389" fill="url(#greyB)"/>
    <polygon points="316,0 338,0 378,389 356,389" fill="url(#bandB)"/>
  </svg>

  <div class="front__person">
    <h1 class="person__name">Marcus Hale, DMP</h1>
    <p class="person__title">President</p>
    <p class="person__email">Marcus@clearlinecommercial.com</p>
    <ul class="phones">
      <li><svg viewBox="0 0 24 24" aria-hidden="true"><path d="M6.6 10.8a15.1 15.1 0 0 0 6.6 6.6l2.2-2.2a1 1 0 0 1 1-.25 11.4 11.4 0 0 0 3.6.57 1 1 0 0 1 1 1V20a1 1 0 0 1-1 1A17 17 0 0 1 3 4a1 1 0 0 1 1-1h3.5a1 1 0 0 1 1 1c0 1.25.2 2.45.57 3.57a1 1 0 0 1-.25 1z"/></svg>(555) 014-2830</li>
      <li><svg viewBox="0 0 24 24" aria-hidden="true"><path d="M6.6 10.8a15.1 15.1 0 0 0 6.6 6.6l2.2-2.2a1 1 0 0 1 1-.25 11.4 11.4 0 0 0 3.6.57 1 1 0 0 1 1 1V20a1 1 0 0 1-1 1A17 17 0 0 1 3 4a1 1 0 0 1 1-1h3.5a1 1 0 0 1 1 1c0 1.25.2 2.45.57 3.57a1 1 0 0 1-.25 1z"/></svg>(555) 014-7716</li>
    </ul>
    <p class="service-area">Serving all of<br>Southern California</p>
    <div class="years-badge" role="img" aria-label="Years of service badge"></div>
  </div>

  <div class="brand front__brand">
    <div class="brand__row"><span class="brand__mark"></span><span class="brand__name">CLEARLINE</span></div>
    <div class="brand__sub">COMMERCIAL BUILDERS</div>
  </div>
  <p class="front__license">License# 1004821</p>
</section>

</body>
</html>
```